Business Card for Multi-Brand Sportswear Company

We are looking for a business card which represents our company and the multiple brands within it.

The company: Kelt Athletic (LTD)
The brands: Kelt, PawaLuni, VerdantFlex, Grit and Gale

Employees using these cards would be representing Kelt Athletic, rather than any of the individual brands. You will see a current design within the uploaded files, to give some inspiration. The actual text of the brands is not necessary, but the logos should be on there is some format.

Our creative minds on this are stretched, so we are looking for someone to make this their own, and show us what a good business card should look like.

We may like to get these printed with spot gloss, so keep that in mind with your designs.

www.keltathletic.co.uk

Industry/Entity Type

Business

Contact Information for Business Card

Tom Hollingsworth-Pryce
Operations Manager
(+44) 1632 960 418
Tom@keltathletic.co.uk
www.keltathletic.co.uk

Font styles to use
Sans Serif
Other font styles liked:
• Eurostile

Colors
ffffff

Requirements
Nice to have
• Dark (black) background

```html
<!DOCTYPE html>
<html lang="en">
<head>
<meta charset="utf-8">
<title>Kelt Athletic – Business Card</title>
<link rel="stylesheet" href="https://fonts.googleapis.com/css2?family=Arimo:wght@400&display=swap">
<style>
  :root {
    --page: #d6d6d6;
    --card-dark: #000000;
    --card-light: #ffffff;
    --brand-grey: #555555;
    --ink: #1a1a1a;
    --accent: #e31e24;
    --brand-purple: #5b4b68;
    --brand-silver: #8a8a8a;
    --divider: #e88a8d;
  }
  * { margin: 0; padding: 0; box-sizing: border-box; }
  html, body {
    width: 1167px; height: 1200px; overflow: hidden;
    background: var(--page);
    font-family: "Arimo", Arial, sans-serif;
  }
  .canvas { position: relative; width: 1167px; height: 1200px; }

  .card { position: absolute; box-shadow: 0 4px 10px rgba(0,0,0,0.25); }
  .card-front { left: 163px; top: 109px; width: 799px; height: 438px; background: var(--card-dark); }
  .card-back { left: 156px; top: 616px; width: 810px; height: 445px; background: var(--card-light); }

  .wordmark {
    position: absolute; display: flex; align-items: center; gap: 16px;
    font-weight: 400; white-space: nowrap; letter-spacing: 1px;
  }
  .wordmark-square { display: block; background: var(--accent); }
  .card-front .wordmark { left: 88px; top: 150px; font-size: 58px; color: var(--brand-grey); }
  .card-front .wordmark-square { width: 22px; height: 22px; }
  .card-back .wordmark { left: 37px; top: 168px; font-size: 33px; color: #000; gap: 10px; }
  .card-back .wordmark-square { width: 13px; height: 13px; }

  .brand-row {
    position: absolute; right: 60px; top: 362px;
    display: flex; align-items: center; gap: 26px;
  }
  .brand-tag { display: flex; align-items: center; gap: 6px; font-size: 15px; font-weight: 400; }
  .brand-tag .dot { width: 12px; height: 12px; display: block; }
  .brand-pawaluni { color: #9a86aa; }
  .brand-pawaluni .dot { background: var(--brand-purple); }
  .brand-verdantflex { color: var(--brand-silver); }
  .brand-verdantflex .dot { border-radius: 50%; border: 2px solid var(--brand-silver); }
  .brand-gritgale { color: var(--accent); }
  .brand-gritgale .dot { background: var(--accent); }

  .divider { position: absolute; left: 430px; top: 117px; width: 2px; height: 218px; background: var(--divider); }

  .contact-name { position: absolute; left: 459px; top: 137px; font-size: 23px; color: var(--accent); white-space: nowrap; }
  .contact-role { position: absolute; left: 482px; top: 171px; font-size: 17.5px; color: var(--ink); }

  .contact-list { position: absolute; left: 458px; top: 220px; list-style: none; }
  .contact-list li {
    display: flex; align-items: center; height: 28px;
    font-size: 17px; color: var(--ink);
  }
  .contact-list svg { width: 17px; height: 17px; margin-right: 10px; flex: none; }
</style>
</head>
<body>
<div class="canvas">

  <section class="card card-front" aria-label="Card front">
    <div class="wordmark"><span class="wordmark-square"></span>Kelt Athletic</div>
    <div class="brand-row">
      <span class="brand-tag brand-pawaluni"><span class="dot"></span>PawaLuni</span>
      <span class="brand-tag brand-verdantflex"><span class="dot"></span>VerdantFlex</span>
      <span class="brand-tag brand-gritgale"><span class="dot"></span>Grit and Gale</span>
    </div>
  </section>

  <section class="card card-back" aria-label="Card back">
    <div class="wordmark"><span class="wordmark-square"></span>Kelt Athletic</div>
    <div class="divider"></div>
    <h1 class="contact-name" style="font-weight:400">Tom Hollingsworth-Pryce</h1>
    <p class="contact-role">Operations Manager</p>
    <ul class="contact-list">
      <li>
        <svg viewBox="0 0 24 24" aria-hidden="true"><path fill="#e31e24" d="M12 1.5a7.5 7.5 0 0 0-7.5 7.5c0 5.6 7.5 13.5 7.5 13.5s7.5-7.9 7.5-13.5A7.5 7.5 0 0 0 12 1.5zm0 10.5a3 3 0 1 1 0-6 3 3 0 0 1 0 6z"/></svg>
        Your Address
      </li>
      <li>
        <svg viewBox="0 0 24 24" aria-hidden="true"><circle cx="12" cy="12" r="10" fill="none" stroke="#e31e24" stroke-width="2"/><path fill="#e31e24" d="M9 6.5l1.8 2.6-1.1 1.3c.7 1.6 1.8 2.7 3.4 3.5l1.3-1.1 2.6 1.7-.8 2.2c-4.3-.3-8-4-8.4-8.4z"/></svg>
        (+44) 1632 960 418
      </li>
      <li>
        <svg viewBox="0 0 24 24" aria-hidden="true"><rect x="2.5" y="5" width="19" height="14" fill="none" stroke="#e31e24" stroke-width="1.8"/><path d="M2.5 5l9.5 8 9.5-8" fill="none" stroke="#e31e24" stroke-width="1.8"/></svg>
        Tom@keltathletic.co.uk
      </li>
      <li>
        <svg viewBox="0 0 24 24" aria-hidden="true" fill="none" stroke="#e31e24" stroke-width="1.6"><circle cx="12" cy="12" r="9.5"/><ellipse cx="12" cy="12" rx="4" ry="9.5"/><path d="M2.5 12h19M4 7h16M4 17h16"/></svg>
        www.keltathletic.co.uk
      </li>
    </ul>
  </section>

</div>
</body>
</html>
```